business card for WRT pty ltd

We require a business card that stands out . I have included our company flyer and would like the services listed to be put on the card so when we Give out the cards to customers they have an idea of services we provide. need the winning design to be in editable photo shop format, editable iMac pages format or editable windows publisher format, so that I can enter in names, email addresses, phone numbers etc myself. I have included a pdf documents of info / items needed on the card to use as reference please.
Updates

need more submissions

Need extra days to review

Sick

Target Market(s)

new customers

Contact Information for Business Card

details are on attached business card requirements file

Requirements
Must have
• I have attached a list of must haves

```html
<!DOCTYPE html>
<html lang="en">
<head>
<meta charset="utf-8">
<title>WRT pty ltd – Business Card</title>
<link href="https://fonts.googleapis.com/css2?family=Fira+Sans+Condensed:wght@500;600;700&family=Montserrat:wght@400;500;600&display=swap" rel="stylesheet">
<style>
  :root {
    --page: #d6d6d4;
    --card-dark: #0b0b0c;
    --card-mid: #1c1c1e;
    --card-sheen: #3a3a3d;
    --text-light: #f2f2f2;
    --text-soft: #cfcfcf;
    --logo-silver: #c4c6c9;
    --truck-sand: #b59a6a;
    --truck-dark: #2a2d33;
  }
  * { box-sizing: border-box; margin: 0; padding: 0; }
  html, body { width: 1200px; height: 675px; overflow: hidden; }
  body {
    background: var(--page);
    position: relative;
    font-family: "Fira Sans Condensed", "Arial Narrow", sans-serif;
  }
  .card {
    position: absolute;
    top: 182px;
    width: 540px;
    height: 310px;
    border-radius: 18px;
    overflow: hidden;
    color: var(--text-light);
    background:
      radial-gradient(ellipse at 30% 20%, var(--card-sheen) 0%, rgba(58,58,61,0) 55%),
      linear-gradient(160deg, var(--card-mid) 0%, var(--card-dark) 60%);
    box-shadow: 0 10px 24px rgba(0,0,0,0.25);
  }
  .card--services { left: 40px; }
  .card--contact { left: 620px; }

  .brand-name {
    position: absolute;
    font-family: "Fira Sans Condensed", "Arial Narrow", sans-serif;
    font-weight: 700;
    color: var(--logo-silver);
    letter-spacing: 2px;
    line-height: 1;
  }
  .card--services .brand-name { left: 58px; top: 30px; font-size: 96px; }
  .card--contact .brand-name { left: 70px; top: 40px; font-size: 104px; }

  .truck-photo {
    position: absolute;
    left: 24px;
    top: 150px;
    width: 270px;
    height: 108px;
    border-radius: 6px;
    background: linear-gradient(90deg, var(--truck-dark) 0%, var(--truck-sand) 40%, #d9cfbf 70%, var(--truck-sand) 100%);
    opacity: 0.9;
  }

  .services {
    position: absolute;
    left: 306px;
    top: 38px;
    width: 220px;
    font-weight: 600;
    font-size: 14px;
    line-height: 17px;
  }
  .services__title { text-transform: uppercase; margin-bottom: 2px; }
  .services__list { list-style: none; }
  .services__list li { padding-left: 11px; position: relative; }
  .services__list li::before {
    content: "";
    position: absolute;
    left: 1px; top: 7px;
    width: 4px; height: 4px;
    border-radius: 50%;
    background: var(--text-light);
  }
  .services__list .services__continued { padding-left: 0; }
  .services__list .services__continued::before { display: none; }

  .person {
    position: absolute;
    right: 40px;
    top: 150px;
    text-align: right;
    font-family: "Montserrat", Arial, sans-serif;
  }
  .person__name { font-size: 19px; font-weight: 500; letter-spacing: 5px; }
  .person__role { font-size: 10px; font-weight: 500; letter-spacing: 3px; margin-top: 6px; color: var(--text-soft); }

  .contact {
    position: absolute;
    left: 38px;
    bottom: 34px;
    font-family: "Montserrat", Arial, sans-serif;
    font-size: 11.5px;
    color: var(--text-soft);
    list-style: none;
  }
  .contact__row { display: flex; align-items: flex-start; gap: 9px; line-height: 16px; }
  .contact__icon { width: 12px; height: 12px; margin-top: 2px; flex: none; fill: var(--text-light); }
  .contact__company { color: var(--text-light); text-transform: uppercase; }
</style>
</head>
<body>

<section class="card card--services">
  <div class="brand-name">WRT</div>
  <div class="truck-photo" role="img" aria-label="Photo of a road train truck hauling tanker trailers"></div>
  <div class="services">
    <p class="services__title">Our Services</p>
    <ul class="services__list">
      <li>Over Size Loads / Hot Shot Loads</li>
      <li>Heavy Vehicle Recovery Services</li>
      <li>Potable Water Deliveries</li>
      <li>Road Building / Maintenance</li>
      <li>Earthworks</li>
      <li>Sand &amp; Metal Supply &amp; Cartage</li>
      <li>Road Train Tippers</li>
      <li>Road Train Tankers</li>
      <li>Road Train Flat Tops</li>
      <li>Drop Deck Trailers</li>
      <li>Mine Site Accredited Equipment</li>
      <li class="services__continued">&amp; Operator</li>
    </ul>
  </div>
</section>

<section class="card card--contact">
  <div class="brand-name">WRT</div>
  <div class="person">
    <p class="person__name">DANIEL HARLOW</p>
    <p class="person__role">DIRECTOR</p>
  </div>
  <ul class="contact">
    <li class="contact__row">
      <svg class="contact__icon" viewBox="0 0 12 12"><path d="M6 0a4 4 0 0 0-4 4c0 3 4 8 4 8s4-5 4-8a4 4 0 0 0-4-4zm0 5.6A1.6 1.6 0 1 1 6 2.4a1.6 1.6 0 0 1 0 3.2z"/></svg>
      <span><span class="contact__company">WRT pty ltd</span><br>Lot 444 example address Australia</span>
    </li>
    <li class="contact__row">
      <svg class="contact__icon" viewBox="0 0 12 12"><path d="M0 2h12v8H0zM1 3l5 3.5L11 3v-.2H1z" fill-rule="evenodd"/></svg>
      <span>email@wrtservices.com.au</span>
    </li>
    <li class="contact__row">
      <svg class="contact__icon" viewBox="0 0 12 12"><path d="M2.5 0.5l2 2.5-1 1.5c.8 1.6 2 2.8 3.6 3.6l1.5-1 2.4 2-1.2 2.2C5.5 11 1 6.5.6 1.6z"/></svg>
      <span>000 444 000</span>
    </li>
    <li class="contact__row">
      <svg class="contact__icon" viewBox="0 0 12 12"><circle cx="6" cy="6" r="5.2" fill="none" stroke="#f2f2f2" stroke-width="1.2"/><path d="M1 6h10M6 .8c-2.4 3-2.4 7.4 0 10.4M6 .8c2.4 3 2.4 7.4 0 10.4" fill="none" stroke="#f2f2f2" stroke-width="1"/></svg>
      <span>www.wrtservices.com.au</span>
    </li>
  </ul>
</section>

</body>
</html>
```